VBN Line Card

We are looking for a line card to leave with potential customers.
Logo on top

VBN is a Colorado-based business specializing in demolition, materials management, hazardous materials management, and trucking & hauling. What differentiates VBN is our breadth of experience in upcycling much of reusable debris from the demolition process for reuse on existing projects or recycling the material for later use on other projects.

We offer an end-to-end client experience that includes seamless communication, budgeting, staffing, on-site organization, and solid, quality work every time.

Trucking and Hauling Equipment:
30 yd End Dump
Steel Side Scrap Trailer
90 yr End Dump
Flatbeds
70 Ton Lowboy Trailer 2-3-2 combo

Gordon Ellery
President
720-463-9170
gellery@vbnmetalworks.com

I'd like it to be easy to read, but look modern

Target Market(s)

General Contractors

Industry/Entity Type

Construction

Colors
EB3D1F
EC4F4E
F09395
F8D3D4
FCEDEE

Requirements
Must have
• Our colors and red and gun metal gray

```html
<!DOCTYPE html>
<html lang="en">
<head>
<meta charset="utf-8">
<title>VBN Line Card</title>
<link rel="stylesheet" href="https://fonts.googleapis.com/css2?family=Rubik:wght@300;700;800&display=swap">
<style>
  :root {
    --backdrop: #d2d3d5;
    --brand-red: #8c161c;
    --gunmetal: #262e34;
    --paper: #ffffff;
  }
  * { margin: 0; padding: 0; box-sizing: border-box; }
  html, body {
    width: 1200px;
    height: 1200px;
    overflow: hidden;
    background: var(--backdrop);
    font-family: "Rubik", sans-serif;
  }
  .card {
    position: absolute;
    left: 200px;
    width: 799px;
  }
  .card-front {
    top: 101px;
    height: 444px;
    background: var(--brand-red);
  }
  .brand-name {
    position: absolute;
    left: 0;
    right: 0;
    top: 152px;
    text-align: center;
    font-weight: 800;
    font-size: 100px;
    letter-spacing: 12px;
    color: var(--paper);
    line-height: 1;
  }
  .card-back {
    top: 651px;
    height: 448px;
    background: var(--paper);
    overflow: hidden;
  }
  .contact {
    position: absolute;
    left: 196px;
    top: 50px;
  }
  .contact-row {
    display: flex;
    align-items: center;
    color: var(--brand-red);
    font-weight: 700;
    text-transform: uppercase;
  }
  .contact-row .icon {
    width: 28px;
    height: 28px;
    margin-right: 14px;
    flex: none;
    fill: var(--gunmetal);
  }
  .person-name { font-size: 39px; line-height: 1; }
  .person-title {
    font-size: 28px;
    margin: 8px 0 0 42px;
    color: var(--brand-red);
    font-weight: 700;
    line-height: 1;
  }
  .phone { font-size: 31px; margin-top: 32px; line-height: 1; }
  .email { font-size: 29px; margin-top: 8px; line-height: 1; }
  .equipment {
    position: absolute;
    left: 0;
    right: 0;
    bottom: 0;
    height: 196px;
    background: var(--gunmetal);
    color: var(--paper);
    text-align: center;
    padding-top: 26px;
  }
  .equipment-heading {
    font-weight: 800;
    font-size: 28px;
    line-height: 1;
    margin-bottom: 9px;
  }
  .equipment-line {
    font-weight: 300;
    font-size: 28px;
    line-height: 35px;
    white-space: nowrap;
  }
  .equipment-line .divider { margin: 0 12px; }
</style>
</head>
<body>
  <section class="card card-front">
    <div class="brand-name">VBN</div>
  </section>

  <section class="card card-back">
    <div class="contact">
      <div class="contact-row person-name">
        <svg class="icon" viewBox="0 0 24 24" aria-hidden="true"><circle cx="12" cy="7" r="4.5"/><path d="M2 23c0-6 4.5-9 10-9s10 3 10 9z"/></svg>
        Gordon Ellery
      </div>
      <div class="person-title">President</div>
      <div class="contact-row phone">
        <svg class="icon" viewBox="0 0 24 24" aria-hidden="true"><path d="M6.6 10.8a15.1 15.1 0 0 0 6.6 6.6l2.2-2.2a1 1 0 0 1 1-.25 11.4 11.4 0 0 0 3.6.57 1 1 0 0 1 1 1V20a1 1 0 0 1-1 1A17 17 0 0 1 3 4a1 1 0 0 1 1-1h3.5a1 1 0 0 1 1 1c0 1.25.2 2.45.57 3.57a1 1 0 0 1-.25 1z"/></svg>
        720-463-9170
      </div>
      <div class="contact-row email">
        <svg class="icon" viewBox="0 0 24 24" aria-hidden="true"><path d="M2 4h20a1 1 0 0 1 1 1v14a1 1 0 0 1-1 1H2a1 1 0 0 1-1-1V5a1 1 0 0 1 1-1zm2.2 3 7.8 6 7.8-6-.9-1.2L12 11.1 5.1 5.8z"/></svg>
        gellery@vbnmetalworks.com
      </div>
    </div>

    <div class="equipment">
      <div class="equipment-heading">TRUCKING AND HAULING EQUIPMENT</div>
      <div class="equipment-line">30 YD END DUMP<span class="divider">|</span>STEEL SIDE SCRAP TRAILER</div>
      <div class="equipment-line">90 YD END DUMP<span class="divider">|</span>FLATBEDS</div>
      <div class="equipment-line">70 TON LOWBOY TRAILER 2-3-2 COMBO</div>
    </div>
  </section>
</body>
</html>
```